Bamboo & Ember Business Card FUN & EXCITING

Here is the Information for the Card:
Harpreet Kalra (Toby)
E: TobyKalra@mailbox-demo.com
C: (480) 555-0147
www.BambooEmberLV.com

We don't want traditional Indian cliche, We a playful bold and fun business card.

Files: https://files.sharebox-demo.net/folders/7QtpLmzR2xVbN4kHs9wYcDfJ3eGaUoPi

https://files.sharebox-demo.net/folders/5ZrqTwyX8mKcE2vBn6aLpHsQ9uFjRgOe

Target Market(s)

Las Vegas Local Restaurant

Industry/Entity Type

Indian Restaurant

Contact Information for Business Card

Name, Email, Cell Phone, Company Logo

```html
<!DOCTYPE html>
<html lang="en">
<head>
<meta charset="utf-8">
<title>Bamboo &amp; Ember — Business Card</title>
<link rel="stylesheet" href="https://fonts.googleapis.com/css2?family=Montserrat:wght@300;400;600;800&display=swap">
<style>
  :root {
    --page-bg: #2a2a2a;
    --card-bg: #1f1f1f;
    --ink: #ffffff;
    --ink-soft: #d9d9d9;
    --accent: #ee7d2b;
    --art-main: #3a3a3a;
    --art-warm: #c8682a;
  }
  * { margin: 0; padding: 0; box-sizing: border-box; }
  html, body {
    width: 1200px; height: 1108px; overflow: hidden;
    background: var(--page-bg);
    font-family: "Montserrat", sans-serif;
    color: var(--ink);
  }
  .card {
    position: absolute;
    width: 704px;
    background: var(--card-bg);
    border-radius: 20px;
    box-shadow: 0 6px 14px rgba(0,0,0,.35);
  }
  .card--front { left: 258px; top: 128px; height: 430px; }
  .card--back  { left: 256px; top: 594px; height: 440px; }

  /* front */
  .brand {
    position: absolute;
    font-weight: 800;
    color: var(--ink);
    line-height: .95;
    text-transform: uppercase;
    letter-spacing: -1px;
  }
  .card--front .brand { left: 0; right: 0; top: 92px; text-align: center; font-size: 46px; }
  .brand-place {
    position: absolute;
    font-weight: 600;
    font-size: 14px;
    color: var(--ink);
  }
  .card--front .brand-place { left: 0; right: 0; top: 196px; text-align: center; }
  .mascot-art {
    position: absolute;
    left: 240px; top: 226px;
    width: 224px; height: 140px;
    border-radius: 14px;
    background: radial-gradient(ellipse at 50% 45%, var(--art-warm) 0%, var(--art-main) 70%);
  }
  .tagline {
    position: absolute; left: 0; right: 0; top: 368px;
    text-align: center; font-size: 11px; color: var(--ink-soft);
    letter-spacing: .3px;
  }

  /* back */
  .card--back .brand { left: 46px; top: 168px; width: 270px; font-size: 44px; }
  .card--back .brand-place { left: 46px; top: 308px; width: 270px; text-align: right; font-size: 15px; }
  .divider {
    position: absolute; left: 354px; top: 150px;
    width: 2px; height: 198px; background: var(--accent);
  }
  .contact { position: absolute; left: 370px; top: 148px; }
  .contact-name { font-size: 26px; font-weight: 600; color: var(--accent); line-height: 1.1; }
  .contact-role { font-size: 16px; font-weight: 300; color: var(--ink-soft); line-height: 1; }
  .contact-list { list-style: none; margin-top: 24px; }
  .contact-list li {
    display: flex; align-items: center; gap: 12px;
    font-size: 16px; font-weight: 400; height: 26px;
  }
  .contact-list svg { width: 15px; height: 15px; fill: var(--accent); flex: none; }
  .contact-address { margin-top: 10px; font-size: 16px; font-weight: 300; line-height: 1.3; }
</style>
</head>
<body>

<section class="card card--front">
  <div class="brand">Bamboo<br>&amp; Ember</div>
  <div class="brand-place">Las Vegas, NV</div>
  <div class="mascot-art" role="img" aria-label="Illustration of two cheerful cartoon food characters walking together, surrounded by small hearts and sparkles"></div>
  <div class="tagline">"A match made in heaven"</div>
</section>

<section class="card card--back">
  <div class="brand">Bamboo<br>&amp; Ember</div>
  <div class="brand-place">Las Vegas, NV</div>
  <div class="divider"></div>
  <div class="contact">
    <div class="contact-name">Harpreet Kalra (Toby)</div>
    <div class="contact-role">owner</div>
    <ul class="contact-list">
      <li>
        <svg viewBox="0 0 16 16" aria-hidden="true"><path d="M2 5c0-2 2-3 6-3s6 1 6 3v1h-3V5H5v1H2zM4 7h8l2 6H2z"/></svg>
        (480) 555-0147
      </li>
      <li>
        <svg viewBox="0 0 16 16" aria-hidden="true"><path d="M1 4h14v1L8 9 1 5zM1 6.5l7 4 7-4V13H1z"/></svg>
        TobyKalra@mailbox-demo.com
      </li>
      <li>
        <svg viewBox="0 0 16 16" aria-hidden="true"><circle cx="8" cy="8" r="7"/><path d="M8 1v14M1 8h14" stroke="#1f1f1f" stroke-width="1.2"/></svg>
        www.BambooEmberLV.com
      </li>
    </ul>
    <div class="contact-address">319 Cedar Ridge Rd, #104<br>Maplewood, OH 43099</div>
  </div>
</section>

</body>
</html>
```